One-Page Flat Design for SEO Company [2 DAYS]

We need a one-page flat design for our SEO company. Our current website is http://www.rankloft.com/. We are looking to completely re-design the site using new flat design techniques.
Below are some examples of the type of style we're going after:
http://quormel.com/
http://tobyrand.co.uk/
https://pentaly.co/
http://milesporter.me/
As you can see- flat, clean, minimal. It is very important you follow this type of style.
For colour scheme, you may use one of the pre-made colour palettes from here:
http://www.vornacle.com/blog/inspiration/24-flat-designs-with-compelling-color-palettes
I've attached a wireframe to be followed.
Hi,

```html
<!DOCTYPE html>
<html lang="en">
<head>
<meta charset="utf-8">
<title>RankLoft – SEO Services</title>
<link rel="stylesheet" href="https://fonts.googleapis.com/css2?family=Open+Sans:wght@400;600;700;800&display=swap">
<style>
:root{
  --orange:#f4a93a;
  --orange-dark:#e39422;
  --ink:#2b2b2b;
  --brown:#4e4844;
  --red:#e85a4f;
  --night:#2e2b32;
  --teal:#3cbfbf;
  --light:#efefef;
  --footer:#34302f;
  --bronze:#f18f2f;
  --silver:#cbc4ba;
  --gold:#f8c41c;
  --platinum:#2fc3e4;
  --white:#ffffff;
  --btn:#2f2c2b;
}
*{box-sizing:border-box;margin:0;padding:0}
html,body{width:1200px;height:3942px;overflow:hidden}
body{font-family:"Open Sans",Arial,sans-serif;color:var(--white);background:var(--footer)}
.section{position:relative;width:1200px;overflow:hidden}
.wrap{width:1120px;margin:0 auto;position:relative}
.btn{display:inline-block;background:var(--btn);color:var(--white);font-weight:600;font-size:20px;padding:10px 22px;border-radius:2px;text-decoration:none;white-space:nowrap}
.section-title{text-align:center;font-weight:800;font-size:38px;letter-spacing:1px;text-transform:uppercase}

/* hero */
.hero{height:613px;background:var(--orange)}
.nav{height:70px;display:flex;align-items:center;justify-content:space-between}
.brand{display:flex;align-items:center;gap:10px}
.brand-mark{width:28px;height:28px;background:var(--white)}
.brand-name{font-weight:800;font-size:30px;color:var(--white);display:block;line-height:1.1}
.brand-tag{font-size:9px;color:var(--white);opacity:.8;display:block}
.nav-links{display:flex;gap:6px;list-style:none}
.nav-links a{display:block;padding:5px 18px;font-size:13px;font-weight:600;color:var(--white);text-decoration:none;letter-spacing:.5px}
.nav-links .active a{background:var(--orange-dark);border:1px solid rgba(255,255,255,.6)}
.hero-body{display:flex;justify-content:space-between;margin-top:40px}
.hero-copy{width:590px}
.hero-copy h1{font-size:48px;line-height:1.2;font-weight:800}
.hero-copy p{font-size:19px;line-height:1.45;margin:24px 0 34px}
.hero-video{width:460px;height:290px;background:linear-gradient(135deg,#3d3d48,#1d1d24);position:relative;margin-top:0}
.hero-video .play{position:absolute;left:50%;top:50%;transform:translate(-50%,-50%)}

/* why */
.why{height:657px;background:var(--brown)}
.why .section-title{padding-top:84px}
.features{display:flex;justify-content:space-between;margin-top:70px;width:1040px}
.feature{width:235px;text-align:center}
.feature svg{height:130px}
.feature h3{font-size:18px;font-weight:600;margin:30px 0 12px;text-transform:uppercase}
.feature p{font-size:14px;line-height:1.55;opacity:.85}

/* packages */
.packages{height:745px;background:var(--red)}
.packages .section-title{padding-top:60px}
.packages .intro{text-align:center;font-size:15px;line-height:1.55;width:860px;margin:18px auto 0}
.plans{display:flex;justify-content:center;margin-top:54px;align-items:flex-start}
.plan{width:240px;background:var(--white);color:var(--ink);text-align:center;height:410px}
.plan-head{height:96px;padding-top:22px;color:var(--white)}
.plan-head h3{font-size:24px;font-weight:800}
.plan-head span{font-size:17px}
.plan ul{list-style:none;padding:36px 0 34px;font-size:16px;line-height:2}
.plan b{font-weight:700}
.plan .btn{font-size:14px;padding:9px 20px}
.plan.bronze .plan-head,.plan.bronze .btn{background:var(--bronze)}
.plan.silver .plan-head,.plan.silver .btn{background:var(--silver)}
.plan.gold{background:var(--gold);height:446px;margin-top:-18px;color:var(--white)}
.plan.gold .plan-head{background:var(--gold);padding-top:40px;height:114px}
.plan.gold .btn{background:var(--white);color:var(--gold)}
.plan.platinum .plan-head,.plan.platinum .btn{background:var(--platinum)}

/* guarantee */
.guarantee{height:175px;background:var(--night)}
.guarantee .wrap{display:flex;justify-content:center;align-items:center;gap:160px;height:175px}
.guarantee h2{font-size:36px;font-weight:400}
.guarantee .btn{background:var(--red);font-size:16px;padding:14px 64px}

/* individual */
.individual{height:591px;background:var(--teal)}
.individual .section-title{padding-top:50px}
.individual .intro{text-align:center;font-size:14px;margin-top:16px}
.services{display:flex;justify-content:center;gap:80px;margin-top:44px}
.service{text-align:center;width:290px}
.service-img{width:220px;height:220px;border-radius:50%;margin:0 auto}
.service h3{font-size:19px;font-weight:700;margin:22px 0 16px;text-transform:uppercase;white-space:nowrap}
.arrow{position:absolute;top:290px}

/* contact */
.contact{height:723px;background:var(--light);color:var(--ink)}
.contact .section-title{padding-top:68px}
.rule{width:1100px;height:1px;background:#cfcfcf;margin:30px auto 0}
.form{width:880px;margin:48px auto 0}
.row{display:flex;justify-content:space-between}
.field{width:425px;height:46px;border:1px solid #bdbdbd;background:var(--white);font-size:14px;padding:13px 16px;color:#555}
.field.message{width:880px;height:196px;margin-top:24px}
.send{display:block;width:130px;margin:40px auto 0;background:var(--red);color:var(--white);text-align:center;font-size:15px;padding:11px 0;border-radius:2px;text-decoration:none}
.socials{display:flex;justify-content:center;gap:70px;margin-top:40px;font-weight:700;font-size:20px}

/* footer */
.footer{height:438px;background:var(--footer);text-align:center}
.footer .brand{justify-content:center;padding-top:92px}
.footer p{font-size:15px;line-height:1.6;margin-top:24px;opacity:.85}
.rings{display:flex;justify-content:center;gap:30px;margin-top:30px}
.ring{width:50px;height:50px;border:2px solid #a9a3a0;border-radius:50%}
</style>
</head>
<body>

<header class="section hero">
  <div class="wrap">
    <nav class="nav">
      <div class="brand"><span class="brand-mark"></span><div><span class="brand-name">RankLoft</span><span class="brand-tag">YOUR SEARCH RANKING PARTNER</span></div></div>
      <ul class="nav-links">
        <li class="active"><a href="#">HOME</a></li><li><a href="#">ABOUT</a></li><li><a href="#">SERVICES</a></li><li><a href="#">FAQ</a></li><li><a href="#">BLOG</a></li><li><a href="#">CONTACT</a></li>
      </ul>
    </nav>
    <div class="hero-body">
      <div class="hero-copy">
        <h1>Boost Your Ranking With Our Guaranteed Seo Services</h1>
        <p>We provide high-quality SEO services that are guaranteed to give your ranking a boost. As of 2015, all of our services are 100% Searchly-friendly and are compatible with the latest Tidal and Harbor updates.</p>
        <a class="btn" href="#">Learn More</a>
      </div>
      <div class="hero-video" role="img" aria-label="Introductory video still about search ranking">
        <svg class="play" width="64" height="64" viewBox="0 0 64 64"><circle cx="32" cy="32" r="30" fill="none" stroke="#fff" stroke-width="3"/><path d="M25 19 L45 32 L25 45Z" fill="#fff"/></svg>
      </div>
    </div>
  </div>
</header>

<section class="section why">
  <h2 class="section-title">Why Choose RankLoft</h2>
  <div class="wrap features">
    <div class="feature">
      <svg viewBox="0 0 80 120" width="80"><text x="40" y="100" text-anchor="middle" font-family="Open Sans,sans-serif" font-weight="800" font-size="110" fill="#fff">$</text></svg>
      <h3>Low Prices</h3><p>Our company prides itself in keeping the prices low for whatever client. You will be pleasantly surprised by our costs.</p>
    </div>
    <div class="feature">
      <svg viewBox="0 0 120 120" width="120"><rect x="10" y="86" width="18" height="30" fill="#fff"/><rect x="36" y="70" width="18" height="46" fill="#fff"/><rect x="62" y="54" width="18" height="62" fill="#fff"/><path d="M20 70 L88 14" stroke="#fff" stroke-width="10"/><path d="M70 6 L104 4 L98 36Z" fill="#fff"/></svg>
      <h3>Increased Ranking</h3><p>The clear power of our backlinks can quickly get your site ranking in a short amount of time, thus reaching more visitors and new leads.</p>
    </div>
    <div class="feature">
      <svg viewBox="0 0 120 120" width="120"><circle cx="60" cy="60" r="40" fill="none" stroke="#fff" stroke-width="14" stroke-dasharray="14 7"/><circle cx="60" cy="60" r="28" fill="#fff"/><text x="60" y="67" text-anchor="middle" font-family="Open Sans,sans-serif" font-weight="800" font-size="20" fill="#4e4844">SEO</text></svg>
      <h3>High Quality Services</h3><p>Our priority is quality and customer satisfaction. By working with us, you can be sure you'll receive top quality service.</p>
    </div>
    <div class="feature">
      <svg viewBox="0 0 100 120" width="100"><path d="M50 6 L92 20 V58 C92 88 70 106 50 114 C30 106 8 88 8 58 V20Z" fill="#fff"/><path d="M30 60 L46 76 L74 44" stroke="#4e4844" stroke-width="10" fill="none"/></svg>
      <h3>100% Safe</h3><p>Our methods are completely safe and white hat. We never use risky tricks that could harm your site.</p>
    </div>
  </div>
</section>

<section class="section packages">
  <h2 class="section-title">RankLoft Packages</h2>
  <p class="intro">The most effective way to improve your rank on Searchly is to build a variety of high quality backlinks to your website. Our hand-picked team of link builders has helped many site owners reach the first page, and our services will surely push your site higher in the results.</p>
  <div class="plans">
    <div class="plan bronze"><div class="plan-head"><h3>BRONZE</h3><span>$39</span></div><ul><li><b>Free</b> feature one</li><li><b>Unlimited</b> feature two</li><li><b>Unlimited</b> feature three</li><li><b>2x</b> feature four</li><li><b>100x</b> feature five</li></ul><a class="btn" href="#">GET STARTED</a></div>
    <div class="plan silver"><div class="plan-head"><h3>SILVER</h3><span>$59</span></div><ul><li><b>Free</b> feature one</li><li><b>Unlimited</b> feature two</li><li><b>Unlimited</b> feature three</li><li><b>2x</b> feature four</li><li><b>100x</b> feature five</li></ul><a class="btn" href="#">GET STARTED</a></div>
    <div class="plan gold"><div class="plan-head"><h3>GOLD</h3><span>$79</span></div><ul><li><b>Free</b> feature one</li><li><b>Unlimited</b> feature two</li><li><b>Unlimited</b> feature three</li><li><b>2x</b> feature four</li><li><b>100x</b> feature five</li></ul><a class="btn" href="#">GET STARTED</a></div>
    <div class="plan platinum"><div class="plan-head"><h3>PLATINUM</h3><span>$109</span></div><ul><li><b>Free</b> feature one</li><li><b>Unlimited</b> feature two</li><li><b>Unlimited</b> feature three</li><li><b>2x</b> feature four</li><li><b>100x</b> feature five</li></ul><a class="btn" href="#">GET STARTED</a></div>
  </div>
</section>

<section class="section guarantee">
  <div class="wrap"><h2>30 Day Money-Back Guarantee</h2><a class="btn" href="#">BUTTON</a></div>
</section>

<section class="section individual">
  <h2 class="section-title">Individual SEO Services</h2>
  <p class="intro">Maybe you don't want to purchase one of our pre-made SEO packages. No problem. We offer a wide range of individual SEO services for your choosing.</p>
  <svg class="arrow" style="left:24px" width="24" height="66" viewBox="0 0 24 66"><path d="M22 2 L4 33 L22 64" stroke="#fff" stroke-width="3" fill="none" opacity=".7"/></svg>
  <svg class="arrow" style="right:24px" width="24" height="66" viewBox="0 0 24 66"><path d="M2 2 L20 33 L2 64" stroke="#fff" stroke-width="3" fill="none" opacity=".7"/></svg>
  <div class="services">
    <div class="service"><div class="service-img" role="img" aria-label="Illustration for blog comment backlinks" style="background:radial-gradient(circle,#f3e7c9,#7bb24a)"></div><h3>Blog Comment Backlinks</h3><a class="btn" href="#">Learn More</a></div>
    <div class="service"><div class="service-img" role="img" aria-label="Illustration for EDU backlinks" style="background:radial-gradient(circle,#ffffff,#4da6d8)"></div><h3>EDU Backlinks</h3><a class="btn" href="#">Learn More</a></div>
    <div class="service"><div class="service-img" role="img" aria-label="Illustration for social bookmarks" style="background:radial-gradient(circle,#e9eef4,#3c78b8)"></div><h3>Social Bookmarks</h3><a class="btn" href="#">Learn More</a></div>
  </div>
</section>

<section class="section contact">
  <h2 class="section-title">Get In Touch</h2>
  <div class="rule"></div>
  <div class="form">
    <div class="row"><div class="field">Your Name</div><div class="field">Your Email</div></div>
    <div class="field message">Your Message</div>
    <a class="send" href="#">SEND</a>
  </div>
  <div class="socials"><span>Facebox</span><span>Chirper</span><span>Circles+</span><span>Linkwell</span></div>
</section>

<footer class="section footer">
  <div class="brand"><span class="brand-mark"></span><div style="text-align:left"><span class="brand-name">RankLoft</span><span class="brand-tag">YOUR SEARCH RANKING PARTNER</span></div></div>
  <p>Fusce dapibus, tellus ac cursus commodo, tortor mauris condimentum<br>Duis mollis, est non commodo luctus, nisi erat porttitor ligula.</p>
  <div class="rings"><span class="ring"></span><span class="ring"></span><span class="ring"></span></div>
</footer>

</body>
</html>
```